Autodetailing namecard design: Rose Gold Lettering on Black Matt

This is a namecard design project
requiring two-sided design
Base Color of Namecard: black matt

On front:
Company name,
"Lumina Finishes 14 Cendana"
Subtext: Auto Detailing Studio

Name of card holder: Marcus Oyelaran
Phone Number: +6011-4837-5062
address: 14, Jalan Cendana 5/3Taman Seri Cendana, 81400 Johor Bahru, Johor, Malaysia

Back:
Our Services
High Gloss Car Paint Protection
Custom Color Modification and Styling
Anti-Chip Glass Protection Film
Heat Rejection Glass Tinting

Target Market(s)

Autodetailing for highend cars

Contact Information for Business Card

as mentioned in project details

Colors

Designer to choose colors to be used in the design.

Requirements
Must have
• The main value-add to this project is the design of a logo suited for our purpose and name, and the inclusion of business card details into the card design

```html
<!DOCTYPE html>
<html lang="en">
<head>
<meta charset="utf-8">
<title>Lumina Finishes 14 Cendana – Business Card</title>
<link rel="stylesheet" href="https://fonts.googleapis.com/css2?family=Fredoka:wght@600;700&family=Arimo:wght@400&display=swap">
<style>
  :root {
    --page: #ffffff;
    --card: #0a0a0a;
    --red: #e8130f;
    --white: #ffffff;
    --silver: #b9bdbd;
    --grey: #5e6162;
  }
  * { margin: 0; padding: 0; box-sizing: border-box; }
  html, body { width: 1200px; height: 1200px; overflow: hidden; background: var(--page); }
  body { position: relative; font-family: "Fredoka", sans-serif; font-weight: 700; }

  .card {
    position: absolute;
    left: 192px;
    width: 816px;
    height: 484px;
    background: var(--card);
  }
  .card--front { top: 76px; }
  .card--back { top: 640px; }

  .abs { position: absolute; line-height: 1; white-space: nowrap; }

  .brand-dot {
    position: absolute;
    border-radius: 50%;
    border: 5px solid var(--grey);
  }
  .brand-name { color: var(--red); font-weight: 700; }

  .tagline {
    font-family: "Arimo", sans-serif;
    font-weight: 400;
    color: var(--white);
    font-size: 20px;
  }

  .holder-name, .holder-phone {
    color: var(--white);
    left: 0; right: 0;
    text-align: center;
  }
  .holder-name { font-size: 40px; }
  .holder-phone { font-size: 42px; display: flex; justify-content: center; align-items: center; gap: 8px; }
  .holder-phone svg { width: 30px; height: 30px; }

  .rule { position: absolute; height: 3px; background: var(--red); }

  .address {
    color: var(--white);
    font-size: 27px;
    left: 0; right: 0;
    text-align: center;
    line-height: 32px;
    white-space: nowrap;
  }

  .services-title { color: var(--red); font-size: 44px; }
  .service {
    color: var(--silver);
    font-size: 25px;
    right: 162px;
    text-align: right;
    letter-spacing: 0.3px;
  }
  .service--double { line-height: 29px; }

  .wheel {
    position: absolute;
    width: 84px; height: 84px;
    border-radius: 50%;
    background: radial-gradient(circle, #e6e8e8 0%, #a9acad 45%, #2b2c2d 62%, #1a1a1a 100%);
  }
</style>
</head>
<body>

  <section class="card card--front">
    <span class="brand-dot" style="left:36px; top:108px; width:62px; height:62px;"></span>
    <div class="abs brand-name" style="left:364px; top:100px; font-size:29px;">LUMINA FINISHES 14 CENDANA</div>
    <div class="abs tagline" style="left:365px; top:139px;">Auto Detailing Studio</div>

    <div class="abs holder-name" style="top:234px;">MARCUS OYELARAN</div>
    <div class="abs holder-phone" style="top:278px;">
      <svg viewBox="0 0 24 24" aria-hidden="true">
        <circle cx="12" cy="12" r="10.5" fill="none" stroke="#fff" stroke-width="1.4"/>
        <path d="M9 6.5c-1.6 1.4-1.6 9.6 0 11l1.4-.6-.6-3.4-1 .2c-.4-1.2-.4-2.8 0-4l1 .2.6-3.4z" fill="#fff"/>
      </svg>
      <span>+6011-4837-5062</span>
    </div>

    <div class="rule" style="left:48px; width:722px; top:364px;"></div>
    <div class="abs address" style="top:376px;">
      14, JALAN CENDANA 5/3TAMAN SERI CENDANA,<br>81400 JOHOR BAHRU, JOHOR, MALAYSIA
    </div>
  </section>

  <section class="card card--back">
    <span class="brand-dot" style="left:52px; top:118px; width:58px; height:58px;"></span>
    <div class="abs brand-name" style="left:124px; top:120px; font-size:22px; line-height:28px; white-space:normal; width:240px;">LUMINA FINISHES 14 CENDANA</div>

    <div class="abs services-title" style="left:384px; top:106px;">: OUR SERVICES :</div>
    <div class="rule" style="left:380px; width:390px; top:156px;"></div>

    <div class="abs service service--double" style="top:170px;">HIGH GLOSS CAR<br>PAINT PROTECTION</div>
    <div class="rule" style="left:48px; width:722px; top:236px;"></div>

    <div class="abs service" style="top:253px;">CUSTOM COLOR MODIFICATION AND STYLING</div>
    <div class="rule" style="left:48px; width:722px; top:289px;"></div>

    <div class="abs service" style="top:306px;">ANTI-CHIP GLASS PROTECTION FILM</div>
    <div class="rule" style="left:48px; width:722px; top:343px;"></div>

    <div class="abs service" style="top:359px;">HEAT REJECTION GLASS TINTING</div>
    <div class="rule" style="left:48px; width:722px; top:397px;"></div>

    <div class="wheel" role="img" aria-label="Car wheel with silver alloy rim" style="left:679px; top:192px;"></div>
    <div class="wheel" role="img" aria-label="Car wheel with silver alloy rim" style="left:679px; top:302px;"></div>
  </section>

</body>
</html>
```